Red Wine Label Design for Wendelhurt / Corvallina

We are a leading Cloud and Service provider in Switzerland: www.wendelhurt-example.ch. For our best customers, we will buy a quantity of red wine from https://www.corvallina-example.ch/Weine-Shop
For this wine, we need a custom label with the following criteria:
- include the tulip from Corvallina
- include the Wendelhurt Logo or the Wendelhurt "W"
- have some kind of relation to our company and/or the IT / Hightech / Cloud Business
- have an exclsive, high-end touch

Target Market(s)

CIO and CEOs

Industry/Entity Type

IT / Cloud Services

Font styles to use
Sans Serif

```html
<!DOCTYPE html>
<html lang="en">
<head>
<meta charset="utf-8">
<title>Wendelhurt Red Wine Label</title>
<link rel="stylesheet" href="https://fonts.googleapis.com/css2?family=Montserrat:wght@300;500;600;700&display=swap">
<style>
  :root {
    --page: #f5f5f5;
    --label-black: #050505;
    --facet-grey: #2b2b2b;
    --red-deep: #7a0f12;
    --red-mid: #c0262b;
    --red-light: #e8676a;
    --red-text: #d6393d;
    --band-text: #1a0a0a;
    --white: #ffffff;
    --emblem-grey: #3a3a3a;
  }
  * { margin: 0; padding: 0; box-sizing: border-box; }
  html, body {
    width: 1200px;
    height: 2271px;
    overflow: hidden;
    background: var(--page);
    font-family: "Montserrat", Arial, sans-serif;
  }
  .label {
    position: absolute;
    left: 60px;
    top: 60px;
    width: 1080px;
    height: 2151px;
    background: var(--label-black);
    overflow: hidden;
  }
  .facet-pattern {
    position: absolute;
    inset: 0;
    background:
      linear-gradient(135deg, var(--facet-grey) 0%, var(--label-black) 35%, #1c1c1c 55%, var(--label-black) 75%, #222 100%);
  }
  .metal-line {
    position: absolute;
    left: 0;
    width: 100%;
    background: linear-gradient(90deg, var(--red-deep), var(--red-light) 30%, var(--red-mid) 60%, var(--red-light) 85%, var(--red-deep));
  }
  .metal-line--top-thin { top: 36px; height: 6px; }
  .metal-line--top-thick { top: 50px; height: 14px; }
  .tulip-emblem {
    position: absolute;
    left: 360px;
    top: 150px;
    width: 360px;
    height: 200px;
    border-radius: 12px;
    background: linear-gradient(90deg, var(--red-deep), var(--red-mid), var(--red-deep));
    opacity: 0.85;
  }
  .brand-mark {
    position: absolute;
    left: 250px;
    top: 420px;
    width: 580px;
    height: 580px;
    border: 14px solid var(--red-mid);
    border-radius: 50%;
    display: flex;
    align-items: center;
    justify-content: center;
  }
  .brand-mark__name {
    color: var(--red-text);
    font-weight: 600;
    font-size: 84px;
    letter-spacing: 1px;
  }
  .security-emblem {
    position: absolute;
    left: 435px;
    top: 1090px;
    width: 210px;
    height: 150px;
    border-radius: 20px;
    background: radial-gradient(ellipse at center, var(--emblem-grey), rgba(40, 40, 40, 0.4) 70%, rgba(20, 20, 20, 0) 100%);
  }
  .name-band {
    position: absolute;
    left: 0;
    top: 1320px;
    width: 100%;
    height: 150px;
  }
  .name-band__rule {
    position: absolute;
    left: 0;
    width: 100%;
    height: 6px;
    background: linear-gradient(90deg, var(--red-deep), var(--red-light), var(--red-deep));
  }
  .name-band__rule--top { top: 0; }
  .name-band__rule--bottom { bottom: 0; }
  .name-band__bar {
    position: absolute;
    left: 0;
    top: 18px;
    width: 100%;
    height: 114px;
    background: linear-gradient(90deg, var(--red-deep), var(--red-mid) 25%, var(--red-light) 55%, var(--red-mid) 80%, var(--red-deep));
    display: flex;
    align-items: center;
    justify-content: center;
  }
  .name-band__text {
    color: var(--band-text);
    font-weight: 700;
    font-size: 80px;
    letter-spacing: 2px;
  }
  .wine-type {
    position: absolute;
    left: 0;
    top: 1510px;
    width: 100%;
    text-align: center;
    color: var(--red-text);
    font-weight: 300;
    font-size: 84px;
    letter-spacing: 2px;
  }
  .volume {
    position: absolute;
    left: 0;
    top: 1930px;
    width: 100%;
    text-align: center;
    color: var(--white);
    font-weight: 600;
    font-size: 50px;
  }
</style>
</head>
<body>
  <div class="label">
    <div class="facet-pattern" role="img" aria-label="Faceted dark grey geometric polygon pattern"></div>
    <div class="metal-line metal-line--top-thin"></div>
    <div class="metal-line metal-line--top-thick"></div>

    <div class="tulip-emblem" role="img" aria-label="Corvallina tulip emblem in metallic red"></div>

    <div class="brand-mark">
      <span class="brand-mark__name">Wendelhurt</span>
    </div>

    <div class="security-emblem" role="img" aria-label="White line emblem for secure cloud services"></div>

    <div class="name-band">
      <div class="name-band__rule name-band__rule--top"></div>
      <div class="name-band__bar"><span class="name-band__text">Wendelhurt</span></div>
      <div class="name-band__rule name-band__rule--bottom"></div>
    </div>

    <div class="wine-type">RED WINE</div>
    <div class="volume">750ml</div>
  </div>
</body>
</html>
```